Killer business card for bowling event and marketing company

Rapid 'Q' Promotions is a sports marketing company that specializes in unique bowling events that provide return on investment for sponsors and memorable experiences for participants and spectators. We need a new business card that simultaneously communicates professionalism and fun. Our preferred colors are black and re

Target Market(s)

Executives in the marketing and sponsorship departments of companies, tourism executives, bowling center owners, and people who love to bowl.

Industry/Entity Type

Business

Contact Information for Business Card

Dean T Walsh
Rapid 'Q' Promotions
PO Box 47
Fairhaven, Oregon USA 22871
Email: deant@rapidqpromotions.com
Mobile: 1-628-518-3762

Requirements
Must have
• Our preferred colors are black and red.
Nice to have
• I am considering the use of the attached image for the back of the card.

```html
<!DOCTYPE html>
<html lang="en">
<head>
<meta charset="utf-8">
<title>Dean T Walsh – Rapid 'Q' Promotions</title>
<link rel="stylesheet" href="https://fonts.googleapis.com/css2?family=Play:wght@400;700&family=Roboto:wght@400;500;700&display=swap">
<style>
  :root {
    --black: #000000;
    --deep-red: #5a0a06;
    --red: #d42a10;
    --orange: #f0701a;
    --yellow: #f7e21e;
    --white: #ffffff;
    --bar: rgba(40, 40, 40, 0.82);
  }
  * { margin: 0; padding: 0; box-sizing: border-box; }
  html, body { width: 1200px; height: 667px; overflow: hidden; background: var(--black); }
  .card { position: relative; width: 1200px; height: 667px; overflow: hidden; background: var(--black); }
  .lane-photo {
    position: absolute; inset: 0;
    background:
      radial-gradient(ellipse 22% 60% at 51% 62%, var(--yellow) 0%, var(--orange) 45%, transparent 80%),
      radial-gradient(ellipse 55% 70% at 51% 58%, var(--red) 0%, rgba(160,20,8,0.8) 50%, transparent 85%),
      linear-gradient(180deg, #1a2a6a 0%, #2a1010 22%, var(--black) 40%, #300804 100%);
  }
  .angles { position: absolute; inset: 0; }
  .name {
    position: absolute; left: 24px; right: 0; top: 150px;
    text-align: center;
    font-family: "Play", sans-serif; font-weight: 400;
    font-size: 120px; line-height: 1; letter-spacing: -3px;
    color: var(--white);
    text-shadow: 4px 4px 0 var(--black), -2px -2px 0 var(--black), 2px -2px 0 var(--black), -2px 2px 0 var(--black);
  }
  .company {
    position: absolute; left: 24px; right: 0; top: 322px;
    text-align: center;
    font-family: "Roboto", Arial, sans-serif; font-weight: 500;
    font-size: 58px; line-height: 1;
    color: var(--white);
    text-shadow: 3px 3px 0 var(--black), -3px -3px 0 var(--black), 3px -3px 0 var(--black), -3px 3px 0 var(--black), 0 3px 0 var(--black), 3px 0 0 var(--black);
  }
  .contact-bar {
    position: absolute; left: 0; right: 0; top: 482px; height: 114px;
    background: var(--bar);
    font-family: "Roboto", Arial, sans-serif; font-size: 24px; color: var(--white);
  }
  .contact-icon { position: absolute; }
  .contact-text { position: absolute; line-height: 29px; white-space: nowrap; }
  .divider { position: absolute; width: 3px; height: 62px; background: var(--white); }
  .phone-icon { left: 29px; top: 44px; }
  .phone-text { left: 76px; top: 50px; }
  .divider-one { left: 276px; top: 30px; }
  .email-icon { left: 312px; top: 42px; }
  .email-text { left: 364px; top: 47px; }
  .divider-two { left: 738px; top: 33px; }
  .pin-icon { left: 770px; top: 44px; }
  .address-text { left: 822px; top: 32px; }
</style>
</head>
<body>
<div class="card">
  <div class="lane-photo" role="img" aria-label="High-contrast photo of a bowling lane with pins in red, orange and yellow and lit screens above"></div>
  <svg class="angles" width="1200" height="667" viewBox="0 0 1200 667" aria-hidden="true">
    <polygon points="0,0 300,0 0,320" fill="var(--deep-red)" opacity="0.85"/>
    <polygon points="0,320 300,0 420,0 0,470" fill="var(--black)" opacity="0.9"/>
    <polygon points="1200,667 1200,300 860,667" fill="var(--deep-red)" opacity="0.85"/>
    <polygon points="820,0 1200,0 1200,300 1150,360" fill="var(--black)" opacity="0.55"/>
  </svg>

  <h1 class="name">Dean T Walsh</h1>
  <p class="company">Rapid 'Q' Promotions</p>

  <div class="contact-bar">
    <svg class="contact-icon phone-icon" width="40" height="40" viewBox="0 0 40 40" aria-hidden="true"><circle cx="20" cy="20" r="18" fill="none" stroke="#fff" stroke-width="2.5"/><path d="M14 11l4 1 1 5-3 2c1 3 3 5 6 6l2-3 5 1 1 4c-1 2-3 3-5 3-8-1-14-7-15-15 0-2 2-4 4-4z" fill="#fff"/></svg>
    <span class="contact-text phone-text">1-628-518-3762</span>
    <div class="divider divider-one"></div>
    <svg class="contact-icon email-icon" width="40" height="40" viewBox="0 0 40 40" aria-hidden="true"><circle cx="20" cy="20" r="18" fill="none" stroke="#fff" stroke-width="2.5"/><rect x="10" y="13" width="20" height="14" fill="none" stroke="#fff" stroke-width="2"/><path d="M10 13l10 8 10-8M10 27l7-6M30 27l-7-6" fill="none" stroke="#fff" stroke-width="2"/></svg>
    <span class="contact-text email-text">deant@rapidqpromotions.com</span>
    <div class="divider divider-two"></div>
    <svg class="contact-icon pin-icon" width="40" height="40" viewBox="0 0 40 40" aria-hidden="true"><circle cx="20" cy="20" r="18" fill="none" stroke="#fff" stroke-width="2.5"/><path d="M20 31c-5-6-8-10-8-14a8 8 0 0 1 16 0c0 4-3 8-8 14z" fill="#fff"/><circle cx="20" cy="17" r="3" fill="var(--black)"/></svg>
    <span class="contact-text address-text">PO Box 47<br>Fairhaven, Oregon USA 22871</span>
  </div>
</div>
</body>
</html>
```